RV BIZ CARDS

Hi,

Is it possible to see a one sided version (with logo and info) as well as a two-sided version (front side w/logo and back side with info)?
How do we choose card stock and finish once we approve a design?

We would like the following info included:

Marcus Trell
Trell Vantage Media
4157 Merrow Crescent, Suite 200
Los Angeles, CA 90068
(323) 555-0192
marcus@trellvantagemedia.example

```html
<!DOCTYPE html>
<html lang="en">
<head>
<meta charset="utf-8">
<title>Trell Vantage Media – Business Cards</title>
<link rel="stylesheet" href="https://fonts.googleapis.com/css2?family=Cabin:wght@400;600;700&display=swap">
<style>
  :root {
    --page-bg: #e9e6e1;
    --card-dark: #262d35;
    --card-light: #f3f3f2;
    --ink: #1b1b1b;
    --ink-soft: #2c2c2c;
    --accent: #7c3a3a;
    --rule: #4a4a4a;
    --white: #ffffff;
  }
  * { margin: 0; padding: 0; box-sizing: border-box; }
  html, body {
    width: 1200px;
    height: 1000px;
    overflow: hidden;
    background: var(--page-bg);
    font-family: "Cabin", sans-serif;
  }
  .canvas { position: relative; width: 1200px; height: 1000px; }
  .card {
    position: absolute;
    left: 250px;
    width: 700px;
    height: 420px;
  }
  .card--front { top: 18px; background: var(--card-dark); }
  .card--back { top: 513px; background: var(--card-light); }

  .front-mark {
    position: absolute;
    left: 50%;
    top: 92px;
    width: 120px;
    height: 120px;
    margin-left: -60px;
    border: 6px solid var(--white);
    border-radius: 50%;
  }
  .front-wordmark {
    position: absolute;
    left: 0;
    right: 0;
    top: 298px;
    text-align: center;
    color: var(--white);
    font-size: 54px;
    font-weight: 400;
    letter-spacing: 5px;
    line-height: 1;
  }

  .back-brand {
    position: absolute;
    left: 108px;
    top: 140px;
    width: 206px;
    text-align: center;
  }
  .back-mark {
    width: 50px;
    height: 50px;
    margin: 0 auto 40px;
    border: 3px solid var(--accent);
    border-radius: 50%;
  }
  .back-wordmark {
    color: var(--ink);
    font-size: 21px;
    font-weight: 400;
    letter-spacing: 2px;
    white-space: nowrap;
  }
  .divider {
    position: absolute;
    left: 332px;
    top: 125px;
    width: 3px;
    height: 160px;
    background: var(--rule);
  }
  .contact {
    position: absolute;
    left: 356px;
    top: 120px;
    color: var(--ink-soft);
    font-size: 18px;
    line-height: 23px;
  }
  .contact__name {
    color: var(--accent);
    font-size: 25px;
    font-weight: 600;
    margin-bottom: 14px;
    line-height: 1.1;
  }
  .contact__company {
    color: var(--ink);
    font-size: 20px;
    font-weight: 700;
    line-height: 26px;
  }
  .contact__line { display: flex; align-items: center; gap: 6px; }
  .contact__icon { width: 15px; height: 15px; flex: none; }
</style>
</head>
<body>
<main class="canvas">
  <section class="card card--front" aria-label="Card front">
    <div class="front-mark" aria-hidden="true"></div>
    <p class="front-wordmark">TRELL VANTAGE</p>
  </section>

  <section class="card card--back" aria-label="Card back">
    <div class="back-brand">
      <div class="back-mark" aria-hidden="true"></div>
      <p class="back-wordmark">TRELL VANTAGE</p>
    </div>
    <div class="divider" aria-hidden="true"></div>
    <div class="contact">
      <p class="contact__name">Marcus Trell</p>
      <p class="contact__company">Trell Vantage Media</p>
      <p>4157 Merrow Crescent, Suite 200</p>
      <p>Los Angeles, CA 90068</p>
      <p class="contact__line">
        <svg class="contact__icon" viewBox="0 0 16 16" aria-hidden="true">
          <path d="M3.5 1.5l2.5 0.5 1 3-1.6 1.2c.8 1.7 2.1 3 3.9 3.9L10.5 8.5l3 1 .5 2.5-1.8 1.8C7 13.5 2.5 9 2.2 3.3z" fill="var(--accent)"/>
        </svg>
        (323) 555-0192
      </p>
      <p class="contact__line">
        <svg class="contact__icon" viewBox="0 0 16 16" aria-hidden="true">
          <rect x="1" y="3.5" width="14" height="10" rx="1" fill="var(--accent)"/>
          <path d="M1.5 4.5L8 9l6.5-4.5" fill="none" stroke="var(--card-light)" stroke-width="1.3"/>
        </svg>
        marcus@trellvantagemedia.example
      </p>
    </div>
  </section>
</main>
</body>
</html>
```